Dorsey K. Wendell Business Card

We need a business card for our company Dorsey K. Wendell Heating & Plumbing to be distributed to potential customers. It should follow the color scheme of our logo and have a modern upscale and masculine look.

The logo is attached and the info below should also be included:

5187 W. Cedar Brook Rd.
Brookvale, PA 17602

Russell T. Wendell
(717) 592-0817
russelltwendell@fernmail.net
dorseykwendell.net
PA #093148

Industry/Entity Type

Business

Contact Information for Business Card

5187 W. Cedar Brook Rd.
Brookvale, PA 17602

Russell T. Wendell
(717) 592-0817
russelltwendell@fernmail.net
dorseykwendell.net
PA #093148

Colors

Designer to choose colors to be used in the design.

Requirements
Must have
• Information above included

```html
<!DOCTYPE html>
<html lang="en">
<head>
<meta charset="UTF-8">
<title>Dorsey K. Wendell Business Card</title>
<link href="https://fonts.googleapis.com/css2?family=Open+Sans:wght@400;600;700;800&display=swap" rel="stylesheet">
<style>
  :root {
    --backdrop: #3b3b3d;
    --card: #1f1f21;
    --card-edge: #2a2a2c;
    --blue: #1a8fe0;
    --green: #7ac943;
    --white: #f2f2f2;
    --emboss-light: #6c6c70;
  }
  * { margin: 0; padding: 0; box-sizing: border-box; }
  html, body {
    width: 799px; height: 1200px; overflow: hidden;
    background: var(--backdrop);
    font-family: "Open Sans", Arial, sans-serif;
  }
  .canvas { position: relative; width: 799px; height: 1200px; }
  .card {
    position: absolute; left: 80px; width: 640px; height: 365px;
    background: var(--card);
    border: 1px solid var(--card-edge);
    box-shadow: 0 10px 24px rgba(0,0,0,.35);
  }
  .card-front { top: 110px; }
  .card-back { top: 700px; }

  .front-mark {
    position: absolute; inset: 0;
    display: flex; align-items: center; justify-content: center; gap: 16px;
  }
  .front-mark .mark-square {
    width: 54px; height: 54px;
    border: 6px solid var(--emboss-light);
  }
  .front-mark .mark-name {
    font-weight: 700; font-size: 30px; letter-spacing: .5px;
    color: var(--emboss-light);
  }

  .holder { position: absolute; left: 32px; top: 30px; }
  .holder-name {
    font-weight: 800; font-size: 23px; color: var(--blue); letter-spacing: .3px;
  }
  .holder-title { font-size: 12.5px; color: var(--white); margin-top: 2px; }
  .contact { position: absolute; left: 32px; top: 178px; list-style: none; }
  .contact li {
    display: flex; align-items: center; gap: 12px;
    font-size: 14px; line-height: 21px; color: var(--white);
  }
  .contact svg { width: 13px; height: 13px; fill: var(--green); flex: none; }
  .contact .accent { color: var(--blue); }
  .address {
    position: absolute; left: 32px; top: 267px;
    font-size: 14px; line-height: 21px; color: var(--white); font-style: normal;
  }
  .company {
    position: absolute; right: 30px; bottom: 36px;
    display: flex; align-items: center; gap: 12px;
  }
  .company .mark-square { width: 38px; height: 38px; background: var(--blue); }
  .company .company-name {
    font-weight: 700; font-size: 18px; line-height: 22px; color: var(--blue);
    width: 200px;
  }
</style>
</head>
<body>
<main class="canvas">
  <section class="card card-front" aria-label="Card front">
    <div class="front-mark">
      <span class="mark-square"></span>
      <span class="mark-name">Dorsey K. Wendell</span>
    </div>
  </section>

  <section class="card card-back" aria-label="Card back">
    <div class="holder">
      <h1 class="holder-name">Russell T. Wendell</h1>
      <p class="holder-title">Managing Director</p>
    </div>

    <ul class="contact">
      <li>
        <svg viewBox="0 0 16 16"><path d="M4 1l3 3-2 2c1 2 3 4 5 5l2-2 3 3-2 3C7 15 1 9 1 3z"/></svg>
        (717) 592-0817
      </li>
      <li>
        <svg viewBox="0 0 16 16"><path d="M1 3h14v10H1z M1 3l7 6 7-6" fill="none" stroke="#7ac943" stroke-width="2"/></svg>
        russelltwendell@fernmail.net
      </li>
      <li>
        <svg viewBox="0 0 16 16"><circle cx="8" cy="8" r="7"/><path d="M1 8h14M8 1c-3 4-3 10 0 14M8 1c3 4 3 10 0 14" stroke="#1f1f21" stroke-width="1.3" fill="none"/></svg>
        <span>www.<span class="accent">dorseykwendell</span>.net</span>
      </li>
      <li>
        <svg viewBox="0 0 16 16"><path d="M5 1L4 15M11 1l-1 14M1 5h14M1 11h14" stroke="#7ac943" stroke-width="2.2" fill="none"/></svg>
        PA #093148
      </li>
    </ul>

    <address class="address">
      5187 W. Cedar Brook Rd.<br>
      Brookvale, PA 17602
    </address>

    <div class="company">
      <span class="mark-square"></span>
      <span class="company-name">Dorsey K. Wendell Heating &amp; Plumbing</span>
    </div>
  </section>
</main>
</body>
</html>
```